Corvanta512 Business Card Redesign

I want to create a design for brand new business cards, I need something exceptional for clear plastic business card design. Please do not submit without it being on a clear design. Photos of the various logo versions attached.

```html
<!DOCTYPE html>
<html lang="en">
<head>
<meta charset="utf-8">
<title>Corvanta512 Business Card</title>
<link href="https://fonts.googleapis.com/css2?family=Poppins:wght@400;500;600;700&display=swap" rel="stylesheet">
<style>
  :root {
    --page: #e7e3dd;
    --frost-top: #f7f8fa;
    --frost-bottom: #e4e7ec;
    --navy: #1b2140;
    --navy-deep: #111631;
    --gold: #c9a159;
    --gold-light: #e2c58a;
    --gold-dark: #a67c37;
    --ink-soft: #d4c7ad;
  }
  html, body {
    margin: 0;
    padding: 0;
    width: 1200px;
    height: 970px;
    overflow: hidden;
    background: var(--page);
    font-family: "Poppins", sans-serif;
  }
  .canvas {
    position: relative;
    width: 1200px;
    height: 970px;
  }
  .card {
    position: absolute;
    left: 100px;
    top: 199px;
    width: 1000px;
    height: 572px;
    overflow: hidden;
    background: linear-gradient(160deg, var(--frost-top), var(--frost-bottom));
    box-shadow: 0 18px 40px rgba(40, 30, 20, 0.22);
  }
  .card-shapes {
    position: absolute;
    inset: 0;
    width: 1000px;
    height: 572px;
  }
  .brand-mark {
    position: absolute;
    left: 151px;
    top: 92px;
    width: 180px;
    height: 180px;
    border-radius: 50%;
    background: var(--navy);
  }
  .brand-name {
    position: absolute;
    left: 60px;
    width: 362px;
    top: 286px;
    text-align: center;
    font-weight: 600;
    font-size: 48px;
    line-height: 60px;
    letter-spacing: 1px;
    color: var(--gold-dark);
    margin: 0;
  }
  .contact-block {
    position: absolute;
    right: 54px;
    top: 310px;
    text-align: right;
  }
  .person-name {
    margin: 0 4px 0 0;
    font-weight: 700;
    font-size: 38px;
    line-height: 1;
    font-variant: small-caps;
    letter-spacing: 0.5px;
    color: var(--ink-soft);
  }
  .person-role {
    margin: 6px 4px 0 0;
    font-weight: 400;
    font-size: 24px;
    color: var(--gold);
  }
  .contact-list {
    list-style: none;
    margin: 32px 0 0;
    padding: 0;
  }
  .contact-item {
    display: flex;
    justify-content: flex-end;
    align-items: center;
    gap: 16px;
    font-size: 25px;
    line-height: 35px;
    color: var(--ink-soft);
  }
  .contact-icon {
    width: 20px;
    height: 20px;
    flex: none;
  }
</style>
</head>
<body>
<div class="canvas">
  <div class="card">
    <svg class="card-shapes" viewBox="0 0 1000 572" aria-hidden="true">
      <defs>
        <linearGradient id="goldBand" x1="0" y1="1" x2="1" y2="0">
          <stop offset="0" stop-color="var(--gold-dark)"/>
          <stop offset="0.6" stop-color="var(--gold)"/>
          <stop offset="1" stop-color="var(--gold-light)"/>
        </linearGradient>
        <linearGradient id="navyField" x1="0" y1="1" x2="1" y2="0">
          <stop offset="0" stop-color="var(--navy)"/>
          <stop offset="1" stop-color="var(--navy-deep)"/>
        </linearGradient>
      </defs>
      <path class="gold-band" d="M0,572 C330,440 640,330 752,0 L1000,0 L1000,8 C760,330 360,470 0,572 Z" fill="url(#goldBand)"/>
      <path class="navy-field" d="M0,572 C360,470 760,330 1000,8 L1000,572 Z" fill="url(#navyField)"/>
    </svg>

    <div class="brand-mark" aria-hidden="true"></div>
    <p class="brand-name">Corvanta512</p>

    <div class="contact-block">
      <p class="person-name">Elena Marsh</p>
      <p class="person-role">Director</p>
      <ul class="contact-list">
        <li class="contact-item">(555) 301-4477
          <svg class="contact-icon" viewBox="0 0 24 24"><path d="M6.6 2.5 9.4 7 7.6 9c1.2 2.6 3 4.6 5.4 6l2-1.8 4.5 2.8-1.3 3.5c-.3.7-1 1.1-1.8 1C9 19.2 4.1 13.4 3 5.6c-.1-.8.3-1.5 1-1.8z" fill="var(--gold)"/></svg>
        </li>
        <li class="contact-item">hello@corvantamail.com
          <svg class="contact-icon" viewBox="0 0 24 24"><rect x="2" y="5" width="20" height="14" fill="var(--gold)"/><path d="M2 5l10 8 10-8" fill="none" stroke="var(--navy)" stroke-width="1.6"/></svg>
        </li>
        <li class="contact-item">www.corvantaweb.com
          <svg class="contact-icon" viewBox="0 0 24 24"><g fill="none" stroke="var(--gold)" stroke-width="1.6"><circle cx="12" cy="12" r="9"/><ellipse cx="12" cy="12" rx="4" ry="9"/><path d="M3 12h18M5 7.5h14M5 16.5h14"/></g></svg>
        </li>
      </ul>
    </div>
  </div>
</div>
</body>
</html>
```